Weihnachtskarte für Personalvermittler im technischen Bereich! als jährliche Danksagung
Das Projekt hat spaß gemacht coole Idee und perfekte Umsetzung
Zielgruppe
Aufgabenstellung
Es soll eine kreative Weihnachtskarte werden, die unser Logo unserer jungen Personalvermittlungsfirma beinhaltet, die hauptsächlich im technischen Bereich unterwegs ist (Kunden sind aus der Energietechnik / Chemieanlagenbau / Anlagenbau / Motorsport /Automobil) .
Eventuell diese Komponenten der Sparten mit in die Karte einfliegen lassen.
Die Weihnachtskarte soll 4 Seiten umfassen (also eine aufklappbare Weihnachtskarte DIN A6 quer ).
Der Text in der Karte soll lauten:
Herzlichen Dank für die gute Zusammenarbeit
Und dass UNS entgegengebrachte Vertrauen.
Wir wünschen Ihnen und Ihrer Familie besinnliche Weihnachtsfeiertage
Und einen erfolgreichen Start in das neue Jahr 2019
Euer TeamBrücke! Team
Maße der Einladungskarte:
DIN A6 quer Einladungskarte (14,8 cm x 10,5 cm), 4-seitiger Druck
Eventuell Adresse mit Logo auf der letzten Seite

```html
<!DOCTYPE html>
<html lang="de">
<head>
<meta charset="utf-8">
<title>Weihnachtskarte TeamBrücke!</title>
<link href="https://fonts.googleapis.com/css2?family=Pacifico&family=Roboto:wght@400;500;700&display=swap" rel="stylesheet">
<style>
  :root {
    --canvas-bg: #ececec;
    --card-dark: #3b4246;
    --card-dark-2: #454d51;
    --card-light: #f4f4f4;
    --accent: #f0a531;
    --ink: #3b4246;
    --white: #ffffff;
    --script: "Pacifico", cursive;
    --sans: "Roboto", Arial, sans-serif;
  }
  * { box-sizing: border-box; margin: 0; padding: 0; }
  html, body { width: 891px; height: 1200px; overflow: hidden; }
  body {
    background: var(--canvas-bg);
    font-family: var(--sans);
    display: flex;
    flex-direction: column;
    align-items: center;
    justify-content: center;
    gap: 70px;
  }
  .spread {
    display: flex;
    width: 800px;
    height: 284px;
    box-shadow: 0 10px 24px rgba(0,0,0,0.18);
  }
  .page {
    position: relative;
    width: 400px;
    height: 284px;
    overflow: hidden;
  }
  .page--dark { background: linear-gradient(135deg, var(--card-dark-2), var(--card-dark)); color: var(--white); }
  .page--light { background: var(--card-light); color: var(--ink); }
  .page + .page { border-left: 1px solid rgba(0,0,0,0.12); }

  /* greeting title */
  .greeting { position: absolute; text-align: right; }
  .greeting__small { display: block; font-weight: 500; font-size: 22px; line-height: 1; margin-right: 40px; }
  .greeting__script { display: block; font-family: var(--script); color: var(--accent); font-size: 36px; line-height: 1.1; }

  /* front cover */
  .cover .greeting { top: 26px; right: 22px; }
  .cover .greeting__small { color: var(--white); }
  .tree-art {
    position: absolute;
    background: linear-gradient(160deg, rgba(240,165,49,0.55), rgba(240,165,49,0.25) 60%, rgba(255,255,255,0.2));
    clip-path: polygon(50% 0, 100% 100%, 0 100%);
  }
  .cover .tree-art { left: 8px; bottom: 8px; width: 200px; height: 262px; }

  /* back cover */
  .imprint {
    position: absolute;
    left: 0; right: 0; bottom: 34px;
    text-align: center;
    font-size: 7.5px;
    font-weight: 700;
    line-height: 1.35;
    color: var(--white);
  }
  .imprint__web {
    display: flex; align-items: center; justify-content: center; gap: 10px;
    margin-top: 6px; font-size: 9px;
  }
  .imprint__web::before, .imprint__web::after {
    content: ""; width: 60px; height: 1px; background: rgba(255,255,255,0.6);
  }

  /* inside left */
  .inside-left .tree-art { left: 110px; top: 22px; width: 180px; height: 190px; }
  .sectors {
    position: absolute; left: 20px; right: 20px; bottom: 22px;
    display: flex; justify-content: space-between; list-style: none;
  }
  .sector {
    flex: 1; text-align: center;
    font-size: 9px; font-weight: 700; line-height: 1.05; text-transform: uppercase;
    padding: 6px 0;
  }
  .sector + .sector { border-left: 1px solid var(--accent); }

  /* inside right */
  .inside-right .greeting { top: 24px; right: 56px; }
  .inside-right .greeting__small { color: var(--ink); }
  .inside-right .greeting__script { font-size: 40px; }
  .new-year {
    position: absolute; left: 20px; right: 20px; top: 108px;
    display: flex; align-items: center; justify-content: center; gap: 10px;
    font-size: 10px; font-weight: 500;
  }
  .new-year::before, .new-year::after { content: ""; width: 44px; height: 1px; background: var(--ink); }
  .message {
    position: absolute; left: 0; right: 0; top: 150px;
    text-align: center; font-size: 10px; font-weight: 500; line-height: 1.3;
  }
  .message__thanks { color: var(--accent); font-weight: 700; margin-bottom: 6px; }
  .signoff {
    position: absolute; left: 0; right: 0; bottom: 28px;
    display: flex; align-items: center; justify-content: center; gap: 6px;
    font-size: 11px; font-weight: 500;
  }
  .signoff__brand { font-size: 15px; font-weight: 500; }
  .signoff__dot { width: 12px; height: 12px; border-radius: 50%; background: var(--accent); }
</style>
</head>
<body>

<section class="spread spread--outside" aria-label="Außenseite">
  <article class="page page--dark back-cover">
    <div class="imprint">
      <p>TeamBrücke Personaldienstleistungen GmbH &amp; Co. KG</p>
      <p>Kelterweg 12 | D-76000 Rebenheim</p>
      <p class="imprint__web">www.teambruecke-personal.de</p>
    </div>
  </article>
  <article class="page page--dark cover">
    <div class="tree-art" role="img" aria-label="Weihnachtsbaum aus orangen und weißen Schneeflocken, Zweigen und Punkten"></div>
    <h1 class="greeting">
      <span class="greeting__small">frohe</span>
      <span class="greeting__script">Weihnachten</span>
    </h1>
  </article>
</section>

<section class="spread spread--inside" aria-label="Innenseite">
  <article class="page page--dark inside-left">
    <div class="tree-art" role="img" aria-label="Weihnachtsbaum aus orangen und weißen Schneeflocken, Zweigen und Punkten"></div>
    <ul class="sectors">
      <li class="sector">Energie<br>Technik</li>
      <li class="sector">Chemie<br>Anlagen Bau</li>
      <li class="sector">Motor<br>Sport</li>
      <li class="sector">Anlagen<br>Bau</li>
      <li class="sector">Auto<br>Mobil</li>
    </ul>
  </article>
  <article class="page page--light inside-right">
    <h2 class="greeting">
      <span class="greeting__small">frohe</span>
      <span class="greeting__script">Weihnachten</span>
    </h2>
    <p class="new-year">und einen guten Start ins neue Jahr 2019</p>
    <div class="message">
      <p class="message__thanks">Herzlichen Dank für die gute Zusammenarbeit!<br>Und dass UNS entgegengebrachte Vertrauen.</p>
      <p>Wir wünschen Ihnen und Ihrer Familie besinnliche Weihnachtsfeiertage<br>Und einen erfolgreichen Start in das neue Jahr 2019</p>
    </div>
    <p class="signoff">
      <span>Euer</span>
      <span class="signoff__dot" aria-hidden="true"></span>
      <span class="signoff__brand">TeamBrücke!</span>
      <span>Team</span>
    </p>
  </article>
</section>

</body>
</html>
```